I need a business card design for a real estate finance, development and management business. We deal with high net worth clients and ask that the business card be neat, clean and sophisticated. We like the attached logo design, font and color and want to incorporate all this into the business card.

Industry/Entity Type

Real Estate

```html
<!DOCTYPE html>
<html lang="en">
<head>
<meta charset="utf-8">
<title>Silver Pond Business Card</title>
<link rel="stylesheet" href="https://fonts.googleapis.com/css2?family=Ubuntu:wght@400;700&display=swap">
<style>
  :root {
    --brand-blue: #1f5fa6;
    --canvas-grey: #e4e5e7;
    --card-white: #ffffff;
    --card-shadow: rgba(0, 0, 0, 0.12);
  }
  html, body {
    margin: 0;
    padding: 0;
    width: 1200px;
    height: 947px;
    overflow: hidden;
    background: var(--canvas-grey);
    font-family: "Ubuntu", sans-serif;
  }
  .stage {
    position: relative;
    width: 1200px;
    height: 947px;
  }
  .card {
    position: absolute;
    top: 330px;
    width: 500px;
    height: 286px;
    background: var(--card-white);
    box-shadow: 0 6px 18px var(--card-shadow);
    box-sizing: border-box;
    color: var(--brand-blue);
  }
  .card-back { left: 70px; }
  .card-front { left: 630px; border-bottom: 4px solid var(--brand-blue); }

  .company-name {
    display: flex;
    align-items: center;
    gap: 0.4em;
    margin: 0;
    font-weight: 400;
    color: var(--brand-blue);
    white-space: nowrap;
  }
  .company-mark {
    display: inline-block;
    width: 0.45em;
    height: 0.45em;
    background: var(--brand-blue);
  }
  .card-front .company-name {
    position: absolute;
    left: 0;
    right: 0;
    top: 116px;
    justify-content: center;
    font-size: 38px;
  }
  .card-back .company-name {
    position: absolute;
    right: 32px;
    bottom: 32px;
    font-size: 22px;
  }

  .holder {
    position: absolute;
    left: 34px;
    top: 30px;
  }
  .holder-name {
    margin: 0;
    font-size: 20px;
    font-weight: 400;
  }
  .holder-name strong { font-weight: 700; }
  .holder-title {
    margin: 2px 0 0;
    font-size: 13px;
  }
  .contact-list {
    position: absolute;
    left: 34px;
    top: 118px;
    margin: 0;
    padding: 0;
    list-style: none;
    font-size: 13.5px;
  }
  .contact-list li {
    display: flex;
    align-items: center;
    gap: 10px;
    height: 22px;
  }
  .contact-icon { width: 14px; height: 14px; fill: var(--brand-blue); }
</style>
</head>
<body>
<main class="stage">
  <section class="card card-back">
    <div class="holder">
      <h1 class="holder-name"><strong>Daniel</strong> R. Whitford</h1>
      <p class="holder-title">Managing Partner</p>
    </div>
    <ul class="contact-list">
      <li>
        <svg class="contact-icon" viewBox="0 0 16 16" aria-hidden="true"><path d="M8 1 1 7.5h2V15h4v-4h2v4h4V7.5h2z"/></svg>
        <span>18 Harbor View Rd. Easton, CT 06612</span>
      </li>
      <li>
        <svg class="contact-icon" viewBox="0 0 16 16" aria-hidden="true"><path d="M3.6 1.5 6 4 4.8 5.9c.9 2 2.3 3.4 4.3 4.3L11 9l2.5 2.4-1.6 2.6C6.5 13.6 2.4 9.5 2 4.1z"/></svg>
        <span>555 218 4470</span>
      </li>
      <li>
        <svg class="contact-icon" viewBox="0 0 16 16" aria-hidden="true"><path d="M1 3h14v10H1zm1.5 1.5v.3L8 9l5.5-4.2v-.3zm0 2.2v4.8h11V6.7L8 10.9z"/></svg>
        <span>dwhitford@silverpondcapital.net</span>
      </li>
    </ul>
    <p class="company-name"><span class="company-mark" aria-hidden="true"></span>Silver Pond</p>
  </section>

  <section class="card card-front">
    <p class="company-name"><span class="company-mark" aria-hidden="true"></span>Silver Pond</p>
  </section>
</main>
</body>
</html>
```